Meadowlark Pet Business Card

We need a business card designed with two sides to it. I would like the front of the card to be mostly graphic and the back of the card to have the bullet points of our pet food.

I don't have a telephone number for the business yet so just leave a space for a toll free number. (800) xxx-xxxx.

Thanks,

Dale
Updates

Combination Diet
Chicken Diet
Beef Diet
Lamb Diet

Website:  www.meadowlarkpet-example.com

email:  tbrowning@meadowlarkpet-example.com

Direct - 555-xxx-xxxx
Toll Free - xxx-xxx-xxxx

www.meadowlarkpet-example.com

Tom Browning (Example)
Customer Experience Officer

tbrowning@meadowlarkpet-example.com
Direct - (555) xxx-xxxx

Sales Inquiries - (800) xxx-xxxx

All,

Please include the following items on the back of the business card.

Combination Diet
Chicken Diet
Beef Diet
Lamb Diet
 

Thanks,

Dale

All, I will also want a QR code on the front or back of the card that can be scanned by a smart phone with our individual contact information.  Thanks, Dale

Industry/Entity Type

Pet

```html
<!DOCTYPE html>
<html lang="en">
<head>
<meta charset="utf-8">
<title>Meadowlark Pet Business Card</title>
<link rel="stylesheet" href="https://fonts.googleapis.com/css2?family=Mulish:wght@300;400;600;700;800&display=swap">
<style>
  :root {
    --backdrop: #d6d6d6;
    --card-dark: #1b1b1b;
    --card-light: #ffffff;
    --accent: #f7c614;
    --text-light: #ffffff;
    --text-dark: #1e1e1e;
    --ghost-light: #e2e2e2;
    --ghost-dark: #232323;
    --silhouette-light: #d0d0d0;
    --silhouette-dark: #111111;
    --sun-haze: #f6ecd6;
  }
  * { box-sizing: border-box; margin: 0; padding: 0; }
  html, body { width: 1200px; height: 717px; overflow: hidden; }
  body {
    position: relative;
    background: var(--backdrop);
    font-family: "Mulish", "Helvetica Neue", Arial, sans-serif;
  }
  .card {
    position: absolute;
    overflow: hidden;
    box-shadow: 0 4px 10px rgba(0,0,0,0.35);
  }
  .card--front {
    left: 316px; top: 31px; width: 535px; height: 321px;
    background: var(--card-dark);
  }
  .card--back {
    left: 316px; top: 374px; width: 533px; height: 320px;
    background: var(--card-dark);
  }
  .front__top {
    position: absolute; left: 0; top: 0; width: 100%; height: 159px;
    background: var(--card-light);
  }
  .sun-haze {
    position: absolute; left: 145px; top: 8px; width: 200px; height: 60px;
    background: radial-gradient(ellipse at center, var(--sun-haze) 0%, rgba(246,236,214,0) 70%);
  }
  .tree-art {
    position: absolute; left: 330px; top: 0; width: 205px; height: 150px;
    background: linear-gradient(180deg, rgba(200,200,200,0.7), rgba(220,220,220,0.25));
    border-radius: 40% 0 0 60%;
    opacity: 0.55;
  }
  .dog-art-light {
    position: absolute; left: 0; top: 70px; width: 95px; height: 89px;
    background: linear-gradient(180deg, var(--silhouette-light), rgba(208,208,208,0.4));
    border-radius: 50% 50% 0 0;
    opacity: 0.7;
  }
  .ghost-name {
    position: absolute; white-space: nowrap; font-weight: 700; letter-spacing: -2px;
    line-height: 1;
  }
  .ghost-name--front {
    left: 150px; top: 82px; font-size: 88px; color: var(--ghost-light);
  }
  .person {
    position: absolute; right: 38px; top: 30px; text-align: right; color: var(--text-dark);
  }
  .person__name { font-size: 21px; font-weight: 300; line-height: 1.1; }
  .person__name strong { font-weight: 800; }
  .person__title { font-size: 11.5px; font-weight: 400; margin-top: 2px; }
  .brand {
    position: absolute; left: 42px; top: 100px; width: 205px;
  }
  .brand__name {
    display: flex; align-items: center; justify-content: center; gap: 8px;
    height: 105px; white-space: nowrap;
    font-size: 21px; font-weight: 800; color: var(--text-light); line-height: 1;
    background: var(--card-dark); border: 3px solid #000;
  }
  .brand__mark { width: 12px; height: 12px; background: var(--accent); flex: none; }
  .brand__tagline {
    margin-top: 10px; text-align: center; font-size: 9.5px; font-weight: 700;
    letter-spacing: 1.2px; color: var(--text-light); white-space: nowrap;
  }
  .contact {
    position: absolute; left: 272px; top: 189px; list-style: none; color: var(--text-light);
    font-size: 12px;
  }
  .contact li { display: flex; align-items: center; gap: 7px; height: 22px; white-space: nowrap; }
  .contact svg { width: 14px; height: 14px; flex: none; }
  .sales { position: absolute; left: 272px; top: 270px; font-size: 12.5px; color: var(--text-light); white-space: nowrap; }
  .sales__label { color: var(--accent); }
  .ghost-name--back-top {
    right: -8px; top: -4px; font-size: 110px; color: var(--ghost-dark);
  }
  .ghost-name--back-bottom {
    left: 10px; bottom: -30px; font-size: 110px; color: var(--ghost-dark);
  }
  .dog-art-dark {
    position: absolute; left: 338px; top: 140px; width: 190px; height: 170px;
    background: linear-gradient(180deg, #141414, var(--silhouette-dark));
    border-radius: 45% 35% 6% 6%;
  }
  .diets {
    position: absolute; left: 62px; top: 64px; list-style: none; color: var(--text-light);
    font-size: 19px; font-weight: 700;
  }
  .diets li { display: flex; align-items: center; gap: 12px; height: 47.5px; }
  .diets li::before {
    content: ""; width: 9px; height: 9px; border-radius: 50%; background: var(--accent);
  }
</style>
</head>
<body>
  <section class="card card--front" aria-label="Business card front">
    <div class="front__top">
      <div class="sun-haze"></div>
      <div class="ghost-name ghost-name--front" aria-hidden="true">meadowlark pet</div>
      <div class="tree-art" role="img" aria-label="Faint acacia tree silhouette"></div>
      <div class="dog-art-light" role="img" aria-label="Faint dog silhouette"></div>
      <div class="person">
        <p class="person__name">Tom <strong>Browning</strong></p>
        <p class="person__title">Customer Experience Officer</p>
      </div>
    </div>
    <div class="brand">
      <div class="brand__name"><span class="brand__mark"></span>Meadowlark Pet</div>
      <p class="brand__tagline">100% NATURAL RAW DOG FOOD</p>
    </div>
    <ul class="contact">
      <li>
        <svg viewBox="0 0 16 16" fill="none" stroke="#f7c614" stroke-width="1.4"><circle cx="8" cy="8" r="6.5"/><ellipse cx="8" cy="8" rx="3" ry="6.5"/><line x1="1.5" y1="8" x2="14.5" y2="8"/></svg>
        meadowlarkpet-example.com
      </li>
      <li>
        <svg viewBox="0 0 16 16"><rect x="1" y="3" width="14" height="10" fill="#f7c614"/><path d="M1 3l7 6 7-6" fill="none" stroke="#1b1b1b" stroke-width="1.3"/></svg>
        tbrowning@meadowlarkpet-example.com
      </li>
      <li>
        <svg viewBox="0 0 16 16" fill="#f7c614"><path d="M1 6c0-2 3-3 7-3s7 1 7 3v1h-3.5V5.5h-7V7H1z"/><rect x="3" y="8" width="10" height="6" rx="1"/></svg>
        555-xxx-xxxx
      </li>
    </ul>
    <p class="sales"><span class="sales__label">Sales Inquiries</span> - (800) xxx-xxxx</p>
  </section>

  <section class="card card--back" aria-label="Business card back">
    <div class="ghost-name ghost-name--back-top" aria-hidden="true">pet</div>
    <div class="ghost-name ghost-name--back-bottom" aria-hidden="true">meadowlark</div>
    <div class="dog-art-dark" role="img" aria-label="Dark silhouette of a standing dog"></div>
    <ul class="diets">
      <li>Combination Diet</li>
      <li>Chicken Diet</li>
      <li>Beef Diet</li>
      <li>Lamb Diet</li>
    </ul>
  </section>
</body>
</html>
```